Full color cover for Chamber's Membership Menu

I need a cover, 8 1/2" x 11" for our Chamber of Commerce Membership Menu. Is should have our logo and the words, Membership Menu on it. That's all that is necessary but it can include one or more of the other photos (maybe a college?) that I added, though they are not required. Our logo colors should be used: 37-170-226, 58-181-74, 40-56-144, 247-148-29, 189-190-192.

Target Market(s)

Business owners and managers

Industry/Entity Type

Business Development

Font styles to use
Serif

Colors
0054AA
0677BA
7BADD7
CADEEF
E8F1F8
00AB8E
00BBA5
67D7C9
C6EFE9
E9F9F6
F0912C
F2A743
F7CA91
FBE8D2
FDF5EE

Requirements
Must have
• Our logo and the words Membership Menu
Nice to have
• An attractive business-like feel. It can be very simple.

```html
<!DOCTYPE html>
<html lang="en">
<head>
<meta charset="utf-8">
<title>Membership Menu Cover</title>
<link href="https://fonts.googleapis.com/css2?family=Archivo:wght@400;800&display=swap" rel="stylesheet">
<style>
  :root{
    --stage:#dcdddf;
    --paper:#f7f7f8;
    --indigo-top:#4a4b9c;
    --indigo:#5059ad;
    --green:#7cc242;
    --green-soft:#6fbb4a;
    --orange:#f7a43a;
    --brand-blue:#2838a0;
    --white:#ffffff;
  }
  *{box-sizing:border-box;margin:0;padding:0}
  html,body{width:1200px;height:1200px;overflow:hidden}
  body{background:var(--stage);position:relative;font-family:"Archivo",Arial,sans-serif}
  .cover{
    position:absolute;left:200px;top:82px;width:800px;height:1035px;
    background:var(--paper);overflow:hidden;
    box-shadow:0 8px 28px rgba(0,0,0,.18);
  }
  .cover-art{position:absolute;inset:0}
  .title{position:absolute;left:72px;top:96px;color:var(--white);font-weight:800;line-height:1}
  .title-line{display:block;font-size:78px;letter-spacing:1px;padding-bottom:14px;border-bottom:1.5px solid rgba(255,255,255,.75)}
  .title-line + .title-line{margin-top:14px;padding-left:22px;width:520px}
  .title-line:first-child{width:470px}
  .photo-grid{
    position:absolute;left:190px;top:300px;width:620px;
    display:grid;grid-template-columns:repeat(3,1fr);gap:7px;
  }
  .photo{height:125px}
  .photo-a{background:linear-gradient(135deg,#5b4a3d,#a7826b)}
  .photo-b{background:linear-gradient(135deg,#b9a7a0,#e3c1c8)}
  .photo-c{background:linear-gradient(135deg,#8fa28c,#c9b8a0)}
  .photo-d{background:linear-gradient(135deg,#6d5248,#c9a48d)}
  .photo-e{background:linear-gradient(135deg,#e3dcd1,#b97b6e)}
  .photo-f{background:linear-gradient(135deg,#4a4038,#d8c6b2)}
  .brand{
    position:absolute;right:48px;bottom:86px;display:flex;align-items:center;gap:14px;
    color:var(--brand-blue);font-weight:800;
  }
  .brand-mark{width:44px;height:44px;border-radius:50%;background:var(--brand-blue)}
  .brand-name{font-size:22px;line-height:1.15;letter-spacing:.5px;text-transform:uppercase}
</style>
</head>
<body>
  <main class="cover">
    <svg class="cover-art" width="800" height="1035" viewBox="0 0 800 1035" aria-hidden="true">
      <defs>
        <linearGradient id="indigoFill" x1="0" y1="0" x2="0" y2="1">
          <stop offset="0" stop-color="var(--indigo-top)"/>
          <stop offset="1" stop-color="var(--indigo)"/>
        </linearGradient>
      </defs>
      <polygon class="left-band" points="0,292 490,672 0,360" fill="var(--green)"/>
      <polygon class="right-triangle" points="806,348 650,508 806,528" fill="var(--green-soft)"/>
      <line class="orange-stripe" x1="806" y1="334" x2="488" y2="668" stroke="var(--orange)" stroke-width="10"/>
      <polygon class="indigo-field" points="0,0 800,0 800,330 482,662 0,292" fill="url(#indigoFill)"/>
    </svg>

    <h1 class="title">
      <span class="title-line">Membership</span>
      <span class="title-line">Menu</span>
    </h1>

    <div class="photo-grid">
      <div class="photo photo-a" role="img" aria-label="Photo of members networking at an evening event"></div>
      <div class="photo photo-b" role="img" aria-label="Photo of a ribbon cutting in front of a storefront"></div>
      <div class="photo photo-c" role="img" aria-label="Photo of a group celebrating a business opening"></div>
      <div class="photo photo-d" role="img" aria-label="Photo of guests posing at a formal chamber dinner"></div>
      <div class="photo photo-e" role="img" aria-label="Photo of two members smiling in an office"></div>
      <div class="photo photo-f" role="img" aria-label="Photo of restaurant staff in aprons"></div>
    </div>

    <div class="brand">
      <span class="brand-mark"></span>
      <span class="brand-name">Riverton Chamber<br>of Commerce &amp; Tourism</span>
    </div>
  </main>
</body>
</html>
```